Business Card Design

The attached file is what i need on the front of the card. No details to be changed.

On the back could i have as a heading:
We buy for cash $$$
Deceased estates house lots
Antiques, vintage furniture, bikes, kitchenware, automobile, toys,
sports memorabilia, books, records, signage,farm equipment and fashion.

Industry/Entity Type

House

```html
<!DOCTYPE html>
<html lang="en">
<head>
<meta charset="utf-8">
<title>We Buy and Sell – Business Card Back</title>
<link rel="stylesheet" href="https://fonts.googleapis.com/css2?family=Lobster+Two:ital,wght@1,700&family=Libre+Franklin:wght@700&family=Quicksand:wght@300;600&family=Arimo&display=swap">
<style>
  :root {
    --paper: #ffffff;
    --ink: #000000;
    --banner-yellow: #ffff00;
    --panel-red: #ff0000;
    --text-white: #ffffff;
  }
  html, body { margin: 0; padding: 0; overflow: hidden; }
  body { width: 1200px; height: 1000px; background: var(--paper); position: relative; font-family: "Quicksand", sans-serif; }
  .print-marks { position: absolute; inset: 0; }
  .card {
    position: absolute; left: 185px; top: 208px; width: 828px; height: 580px;
    border: 2px solid var(--ink); overflow: hidden;
  }
  .banner {
    position: absolute; left: 0; top: 0; width: 100%; height: 160px;
    background: var(--banner-yellow); border-bottom: 1px solid var(--ink); text-align: center;
  }
  .banner-title {
    position: absolute; left: 0; right: 0; top: 0; margin: 0;
    font-family: "Lobster Two", cursive; font-style: italic; font-weight: 700;
    font-size: 60px; line-height: 76px; letter-spacing: 5px; color: var(--ink);
    text-shadow: -2px -2px 0 #fff, 2px -2px 0 #fff, -2px 2px 0 #fff, 2px 2px 0 #fff, 0 2px 0 #fff, 0 -2px 0 #fff, 2px 0 0 #fff, -2px 0 0 #fff, 4px 4px 0 var(--ink);
  }
  .sparkle { position: absolute; top: 20px; color: var(--text-white); font-size: 30px; }
  .sparkle.left { left: 100px; } .sparkle.right { right: 104px; }
  .banner-list {
    position: absolute; left: 0; right: 0; top: 72px; margin: 0;
    font-family: "Libre Franklin", sans-serif; font-weight: 700; font-size: 22px; line-height: 26.5px;
    letter-spacing: 0.5px; color: var(--ink);
  }
  .stock {
    position: absolute; left: 0; top: 161px; width: 100%; bottom: 0;
    background: var(--panel-red); color: var(--text-white); text-align: center;
  }
  .stock-list { list-style: none; margin: 0; padding: 14px 0 0; }
  .stock-item { font-weight: 300; font-size: 19.5px; line-height: 33px; height: 33px; }
  .stock-item.wrap { line-height: 27px; height: 54px; margin-bottom: 6px; }
  .stock-label { font-weight: 600; font-size: 26px; line-height: 0; }
  .stock-extra { font-weight: 600; font-size: 27px; line-height: 40px; height: 40px; margin: 0; }
  .stock-note { position: absolute; right: 18px; bottom: 10px; margin: 0; font-weight: 300; font-size: 19px; line-height: 24px; }
  .slug { position: absolute; top: 830px; font-family: "Arimo", sans-serif; font-size: 13px; color: var(--ink); }
  .slug.left { left: 189px; } .slug.right { right: 174px; }
</style>
</head>
<body>
<svg class="print-marks" width="1200" height="1000" viewBox="0 0 1200 1000" aria-hidden="true">
  <defs>
    <g id="reg-target">
      <circle r="10" fill="none" stroke="#000" stroke-width="1.5"/>
      <circle r="5.5" fill="#000"/>
      <line x1="-14" y1="0" x2="14" y2="0" stroke="#000" stroke-width="1.2"/>
      <line x1="0" y1="-14" x2="0" y2="14" stroke="#000" stroke-width="1.2"/>
      <line x1="-5.5" y1="0" x2="5.5" y2="0" stroke="#fff" stroke-width="1.2"/>
      <line x1="0" y1="-5.5" x2="0" y2="5.5" stroke="#fff" stroke-width="1.2"/>
    </g>
  </defs>
  <g class="tone-bar" stroke="#000" stroke-width="1">
    <rect x="180" y="145" width="31" height="31" fill="#000"/>
    <rect x="211" y="145" width="31" height="31" fill="#0a0a0a"/>
    <rect x="242" y="145" width="31" height="31" fill="#111"/>
    <rect x="273" y="145" width="31" height="31" fill="#1c1c1c"/>
    <rect x="304" y="145" width="31" height="31" fill="#2e2e2e"/>
    <rect x="335" y="145" width="31" height="31" fill="#444"/>
    <rect x="366" y="145" width="31" height="31" fill="#636363"/>
    <rect x="397" y="145" width="31" height="31" fill="#868686"/>
    <rect x="428" y="145" width="31" height="31" fill="#a8a8a8"/>
    <rect x="459" y="145" width="31" height="31" fill="#d0d0d0"/>
    <rect x="490" y="145" width="27" height="31" fill="#fff"/>
  </g>
  <g class="colour-bar" stroke="#000" stroke-width="1">
    <rect x="683" y="145" width="31" height="31" fill="#ffff00"/>
    <rect x="714" y="145" width="31" height="31" fill="#ff00ff"/>
    <rect x="745" y="145" width="31" height="31" fill="#00ffff"/>
    <rect x="776" y="145" width="31" height="31" fill="#0000ff"/>
    <rect x="807" y="145" width="31" height="31" fill="#00ff00"/>
    <rect x="838" y="145" width="31" height="31" fill="#ff0000"/>
    <rect x="869" y="145" width="31" height="31" fill="#000"/>
    <rect x="900" y="145" width="31" height="31" fill="#ffff80"/>
    <rect x="931" y="145" width="31" height="31" fill="#ff80ff"/>
    <rect x="962" y="145" width="31" height="31" fill="#80ffff"/>
    <rect x="993" y="145" width="27" height="31" fill="#808080"/>
  </g>
  <g class="crop-marks" stroke="#000" stroke-width="1">
    <line x1="166" y1="145" x2="166" y2="177"/>
    <line x1="1033" y1="145" x2="1033" y2="177"/>
    <line x1="122" y1="189" x2="153" y2="189"/>
    <line x1="1047" y1="189" x2="1080" y2="189"/>
    <line x1="122" y1="808" x2="153" y2="808"/>
    <line x1="1047" y1="808" x2="1080" y2="808"/>
    <line x1="166" y1="822" x2="166" y2="857"/>
    <line x1="1033" y1="822" x2="1033" y2="857"/>
  </g>
  <use href="#reg-target" x="600" y="160"/>
  <use href="#reg-target" x="136" y="500"/>
  <use href="#reg-target" x="1064" y="500"/>
  <use href="#reg-target" x="600" y="838"/>
</svg>

<section class="card">
  <header class="banner">
    <span class="sparkle left">✦</span>
    <h1 class="banner-title">We buy and sell</h1>
    <span class="sparkle right">✦</span>
    <p class="banner-list">Deceased Estates, House Lots, Antiques, Vintage Furniture, Bikes,<br>Kitchenware, Automobile, Toys, Sports Memorabilia, Books, Records,<br>Signage, Farm Equipment and Fashion.</p>
  </header>
  <div class="stock">
    <ul class="stock-list">
      <li class="stock-item"><span class="stock-label">Ceramics:</span> from all eras and from all over the world</li>
      <li class="stock-item"><span class="stock-label">Furniture:</span> rustic, restored, chairs, teak, tables</li>
      <li class="stock-item"><span class="stock-label">Clothes:</span> mens &amp; ladies, shirts, dresses, shoes, jewellery</li>
      <li class="stock-item wrap"><span class="stock-label">Glassware:</span> depression glass, uranium, retro, murano,<br>Scandinavian, Czechoslovakian</li>
      <li class="stock-item"><span class="stock-label">Bikes:</span> dragsters, skateboards &amp; bike parts</li>
      <li class="stock-item"><span class="stock-label">Kitchenalia:</span> canisters, glasses, utensils items from all eras</li>
      <li class="stock-item"><span class="stock-label">Books:</span> from all eras</li>
      <li class="stock-item"><span class="stock-label">Records:</span> a variety of eras 50s, 60s, 70s, 80s</li>
      <li class="stock-item"><span class="stock-label">Toys:</span> model cars, pedal cars, dolls</li>
    </ul>
    <p class="stock-extra">Coins &amp; Stamps, Military &amp; Watches and so much more</p>
    <p class="stock-note">Stallholder enquiries welcome</p>
  </div>
</section>

<span class="slug left">48064 Vintage Postcard.indd &nbsp;2</span>
<span class="slug right">18/10/13 &nbsp;&nbsp;1:58 PM</span>
</body>
</html>
```